Marlow Realty Real Estate Brokerage Recruiting Flyer

We are a real estate brokerage looking to hire more real estate agents. We need to list everything we have to offer as a company so real estate agents will join our company. this is our company website: www.Marlowrealty.example .

100% COMMISSION NO MONTHLY FEE
$450 Flat Transaction FEE

What We Offer:
24/7 Office Access
Free E & O Insurance for 1st Year
Free Online CE and PLE
Free 1,000 Business Cards
Free Professional Social Media Marketing
Free Printing, Scanning, and Copies
Free Buyer and Seller Presentation Packages
Free Filquay Cloud Based Document Management Access
Access to our Internal Brokerage Forum
Company Profit Sharing!
Private Offices Available to Rent

*Lead Generation Software with over 3,000 Leads
*10 Leads to Start
* Free Personal CRM and Website
*Restrictions and Rules apply

Company Address:
4817 Amberfield Road
Suite 512
Fairfax, VA 22194
Phone: 703-555-0147
email: info@marlowrealty.example

Target Market(s)

Real Estate Agents

Industry/Entity Type

Real Estate

Colors
0555a3
ffffff

Requirements
Must have
• 100% COMMISSION NO MONTHLY FEE
$450 Flat Transaction FEE

What We Offer:
24/7 Office Access
Free Online CE and PLE
Free 1,000 Business Cards
Company Profit Sharing!

*10 Leads to Start

Company Address:
4817 Amberfield Road
Suite 512
Fairfax, VA 22194
Phone: 703-555-0147

```html
<!DOCTYPE html>
<html lang="en">
<head>
<meta charset="utf-8">
<title>Marlow Realty – Agent Recruiting Flyer</title>
<link href="https://fonts.googleapis.com/css2?family=Oswald:wght@500;600&family=Roboto:wght@300;400;500;700;900&display=swap" rel="stylesheet">
<style>
  :root {
    --brand-blue: #0555a3;
    --navy: #0b3f86;
    --light-blue: #7fc1ff;
    --white: #ffffff;
    --ink: #1f2b44;
    --footer-dark: #3a3a3c;
    --stage: #e9e9eb;
  }
  * { box-sizing: border-box; margin: 0; padding: 0; }
  html, body { width: 1200px; height: 1200px; overflow: hidden; background: var(--stage); }
  body { font-family: "Roboto", Arial, sans-serif; color: var(--ink); }

  .flyer {
    position: absolute; left: 175px; top: 0;
    width: 850px; height: 1200px; background: var(--white); overflow: hidden;
  }
  .flyer-art { position: absolute; inset: 0; }

  .brand { position: absolute; left: 40px; top: 74px; display: flex; align-items: center; gap: 10px; }
  .brand-square { width: 28px; height: 28px; background: var(--brand-blue); }
  .brand-name { font-size: 28px; font-weight: 500; color: var(--brand-blue); letter-spacing: 0.5px; white-space: nowrap; }

  .offer-badge {
    position: absolute; left: 100px; top: 500px; width: 280px; height: 280px;
    display: flex; flex-direction: column; align-items: center; justify-content: center;
    font-family: "Oswald", "Arial Narrow", sans-serif; font-weight: 600;
    text-transform: uppercase; line-height: 1.08; text-align: center; white-space: nowrap;
  }
  .offer-badge .strong { color: var(--white); font-size: 32px; }
  .offer-badge .soft { color: var(--light-blue); font-size: 32px; }
  .offer-badge .divider { width: 200px; border-top: 2px dotted var(--white); margin: 10px 0; }

  .perks { position: absolute; left: 508px; top: 492px; width: 318px; }
  .perks-title { font-size: 21px; font-weight: 900; color: var(--navy); margin-bottom: 6px; }
  .perk-list { list-style: none; }
  .perk {
    display: flex; gap: 7px; font-size: 15.5px; font-weight: 500; line-height: 1.25;
    color: var(--ink); margin-bottom: 4px;
  }
  .tick { flex: 0 0 14px; width: 14px; height: 14px; margin-top: 3px; }
  .free-tag {
    display: inline-block; background: var(--brand-blue); color: var(--white);
    font-size: 11px; font-weight: 900; padding: 1px 5px; border-radius: 3px;
    border: 1.5px solid var(--white); box-shadow: 0 0 0 1px var(--brand-blue);
    margin-right: 5px; vertical-align: 1px;
  }

  .extras { position: absolute; left: 56px; top: 830px; width: 370px; list-style: none; }
  .extras .perk { font-size: 18px; margin-bottom: 8px; }
  .extras .tick { margin-top: 4px; }

  .contact { position: absolute; left: 610px; top: 1000px; color: var(--white); }
  .contact-label { font-size: 22px; font-weight: 300; letter-spacing: 0.5px; }
  .contact-phone { font-size: 33px; font-weight: 900; }

  .footer {
    position: absolute; left: 0; top: 1100px; width: 850px; height: 100px;
    color: var(--white); font-size: 15px; font-weight: 400;
  }
  .footer .address { position: absolute; left: 56px; top: 26px; }
  .footer .email { position: absolute; left: 56px; top: 54px; }
  .footer .web { position: absolute; left: 430px; top: 54px; }
</style>
</head>
<body>
<main class="flyer">
  <svg class="flyer-art" width="850" height="1200" viewBox="0 0 850 1200" xmlns="http://www.w3.org/2000/svg">
    <defs>
      <linearGradient id="photoTone" x1="0" y1="0" x2="0" y2="1">
        <stop offset="0" stop-color="#6fa6e6"/>
        <stop offset="0.35" stop-color="#c9b79a"/>
        <stop offset="0.65" stop-color="#8a5a45"/>
        <stop offset="1" stop-color="#5f9a3a"/>
      </linearGradient>
      <linearGradient id="panelTone" x1="0" y1="0" x2="1" y2="1">
        <stop offset="0" stop-color="#f2f2f3"/>
        <stop offset="1" stop-color="#d9d9dc"/>
      </linearGradient>
      <radialGradient id="badgeTone" cx="0.5" cy="0.4" r="0.6">
        <stop offset="0" stop-color="#1a6fc4"/>
        <stop offset="1" stop-color="#0a3f87"/>
      </radialGradient>
    </defs>

    <path class="hero-photo" role="img" aria-label="Photo of a smiling agent in a suit in front of a brick suburban house"
          d="M0,0 H850 V360 C600,360 400,440 390,640 C360,690 300,705 0,705 Z" fill="url(#photoTone)"/>

    <path class="logo-corner" d="M0,0 H330 C330,180 220,300 0,320 Z" fill="var(--white)"/>
    <path d="M330,0 C330,180 220,300 0,320" fill="none" stroke="var(--brand-blue)" stroke-width="10"/>

    <path class="perks-panel" d="M850,360 C600,360 400,440 390,640 C380,820 480,905 640,935 C720,952 790,955 850,955 Z"
          fill="url(#panelTone)" stroke="var(--brand-blue)" stroke-width="9"/>

    <circle cx="240" cy="640" r="168" fill="#b9babd"/>
    <circle cx="240" cy="640" r="154" fill="url(#badgeTone)"/>

    <path class="contact-band" d="M440,1100 C520,1020 650,975 850,950 V1100 Z" fill="var(--brand-blue)"/>
    <rect class="footer-bar" x="0" y="1100" width="850" height="100" fill="var(--footer-dark)"/>

    <circle cx="530" cy="1045" r="62" fill="#c9cacd"/>
    <circle cx="530" cy="1045" r="52" fill="var(--white)"/>
    <path d="M505,1020 l12,-4 l8,16 l-7,6 c4,10 11,17 21,21 l6,-7 l16,8 l-4,12 c-30,2 -55,-22 -52,-52 Z" fill="var(--brand-blue)"/>
    <path d="M535,1020 a20,20 0 0 1 20,20 M537,1007 a33,33 0 0 1 31,31" fill="none" stroke="var(--brand-blue)" stroke-width="4" stroke-linecap="round"/>
  </svg>

  <div class="brand">
    <span class="brand-square"></span>
    <span class="brand-name">Marlow Realty</span>
  </div>

  <div class="offer-badge">
    <span class="strong">100% Commission</span>
    <span class="soft">No Monthly Fee</span>
    <span class="divider"></span>
    <span class="strong">$450 Flat</span>
    <span class="soft">Transaction Fee</span>
  </div>

  <section class="perks">
    <h2 class="perks-title">WHAT WE OFFER:</h2>
    <ul class="perk-list">
      <li class="perk"><svg class="tick" viewBox="0 0 16 16"><circle cx="8" cy="8" r="6.5" fill="none" stroke="#0555a3" stroke-width="1.6"/><path d="M5 8.2l2 2 4-4" fill="none" stroke="#0555a3" stroke-width="1.6"/></svg><span>24/7 Office Access</span></li>
      <li class="perk"><svg class="tick" viewBox="0 0 16 16"><circle cx="8" cy="8" r="6.5" fill="none" stroke="#0555a3" stroke-width="1.6"/><path d="M5 8.2l2 2 4-4" fill="none" stroke="#0555a3" stroke-width="1.6"/></svg><span><span class="free-tag">FREE</span>E &amp; O Insurance for 1st Year</span></li>
      <li class="perk"><svg class="tick" viewBox="0 0 16 16"><circle cx="8" cy="8" r="6.5" fill="none" stroke="#0555a3" stroke-width="1.6"/><path d="M5 8.2l2 2 4-4" fill="none" stroke="#0555a3" stroke-width="1.6"/></svg><span><span class="free-tag">FREE</span>Online CE and PLE</span></li>
      <li class="perk"><svg class="tick" viewBox="0 0 16 16"><circle cx="8" cy="8" r="6.5" fill="none" stroke="#0555a3" stroke-width="1.6"/><path d="M5 8.2l2 2 4-4" fill="none" stroke="#0555a3" stroke-width="1.6"/></svg><span><span class="free-tag">FREE</span>1,000 Business Cards</span></li>
      <li class="perk"><svg class="tick" viewBox="0 0 16 16"><circle cx="8" cy="8" r="6.5" fill="none" stroke="#0555a3" stroke-width="1.6"/><path d="M5 8.2l2 2 4-4" fill="none" stroke="#0555a3" stroke-width="1.6"/></svg><span><span class="free-tag">FREE</span>Professional Social Media Marketing</span></li>
      <li class="perk"><svg class="tick" viewBox="0 0 16 16"><circle cx="8" cy="8" r="6.5" fill="none" stroke="#0555a3" stroke-width="1.6"/><path d="M5 8.2l2 2 4-4" fill="none" stroke="#0555a3" stroke-width="1.6"/></svg><span><span class="free-tag">FREE</span>Printing, Scanning, and Copies</span></li>
      <li class="perk"><svg class="tick" viewBox="0 0 16 16"><circle cx="8" cy="8" r="6.5" fill="none" stroke="#0555a3" stroke-width="1.6"/><path d="M5 8.2l2 2 4-4" fill="none" stroke="#0555a3" stroke-width="1.6"/></svg><span><span class="free-tag">FREE</span>Buyer and Seller Presentation Packages</span></li>
      <li class="perk"><svg class="tick" viewBox="0 0 16 16"><circle cx="8" cy="8" r="6.5" fill="none" stroke="#0555a3" stroke-width="1.6"/><path d="M5 8.2l2 2 4-4" fill="none" stroke="#0555a3" stroke-width="1.6"/></svg><span><span class="free-tag">FREE</span>Filquay Cloud Based Document Management Access</span></li>
      <li class="perk"><svg class="tick" viewBox="0 0 16 16"><circle cx="8" cy="8" r="6.5" fill="none" stroke="#0555a3" stroke-width="1.6"/><path d="M5 8.2l2 2 4-4" fill="none" stroke="#0555a3" stroke-width="1.6"/></svg><span>Access to our Internal Brokerage Forum</span></li>
      <li class="perk"><svg class="tick" viewBox="0 0 16 16"><circle cx="8" cy="8" r="6.5" fill="none" stroke="#0555a3" stroke-width="1.6"/><path d="M5 8.2l2 2 4-4" fill="none" stroke="#0555a3" stroke-width="1.6"/></svg><span>Company Profit Sharing!</span></li>
      <li class="perk"><svg class="tick" viewBox="0 0 16 16"><circle cx="8" cy="8" r="6.5" fill="none" stroke="#0555a3" stroke-width="1.6"/><path d="M5 8.2l2 2 4-4" fill="none" stroke="#0555a3" stroke-width="1.6"/></svg><span>Private Offices Available to Rent</span></li>
    </ul>
  </section>

  <ul class="extras">
    <li class="perk"><svg class="tick" viewBox="0 0 16 16"><circle cx="8" cy="8" r="6.5" fill="none" stroke="#0555a3" stroke-width="1.6"/><path d="M5 8.2l2 2 4-4" fill="none" stroke="#0555a3" stroke-width="1.6"/></svg><span>Lead Generation Software with over 3,000 Leads</span></li>
    <li class="perk"><svg class="tick" viewBox="0 0 16 16"><circle cx="8" cy="8" r="6.5" fill="none" stroke="#0555a3" stroke-width="1.6"/><path d="M5 8.2l2 2 4-4" fill="none" stroke="#0555a3" stroke-width="1.6"/></svg><span>10 Leads to Start</span></li>
    <li class="perk"><svg class="tick" viewBox="0 0 16 16"><circle cx="8" cy="8" r="6.5" fill="none" stroke="#0555a3" stroke-width="1.6"/><path d="M5 8.2l2 2 4-4" fill="none" stroke="#0555a3" stroke-width="1.6"/></svg><span><span class="free-tag">FREE</span>Personal CRM and Website</span></li>
    <li class="perk"><svg class="tick" viewBox="0 0 16 16"><circle cx="8" cy="8" r="6.5" fill="none" stroke="#0555a3" stroke-width="1.6"/><path d="M5 8.2l2 2 4-4" fill="none" stroke="#0555a3" stroke-width="1.6"/></svg><span>Restrictions and Rules apply</span></li>
  </ul>

  <div class="contact">
    <div class="contact-label">CONTACT US</div>
    <div class="contact-phone">703-555-0147</div>
  </div>

  <footer class="footer">
    <div class="address">4817 Amberfield Road Suite 512 Fairfax, VA 22194</div>
    <div class="email">&#9993; info@marlowrealty.example</div>
    <div class="web">&#9901; www.Marlowrealty.example</div>
  </footer>
</main>
</body>
</html>
```